Pomvel stationary merch

We are going to sell a collection of notebooks of different styles but under same theme. Our theme is inspired by the planets of space in pastel colors. For example, one notebook of the collection is based on Planet Earth so that it is is pastel green color with a minimalistic sketch of planet Earth.

```html
<!DOCTYPE html>
<html lang="en">
<head>
<meta charset="utf-8">
<title>Earth Notebook – Cover and Page</title>
<link href="https://fonts.googleapis.com/css2?family=Open+Sans:wght@300;400;700&display=swap" rel="stylesheet">
<style>
  :root {
    --canvas: #ffffff;
    --cream: #f4eac5;
    --pastel-teal: #bdd9d4;
    --pattern-tint: #e6e5c9;
    --rule-blue: #86b4c1;
  }
  html, body {
    margin: 0;
    padding: 0;
    width: 1200px;
    height: 1200px;
    overflow: hidden;
    background: var(--canvas);
  }
  .stage {
    position: relative;
    width: 1200px;
    height: 1200px;
  }
  .sheet {
    position: absolute;
    top: 274px;
    width: 467px;
    height: 660px;
    background: var(--cream);
    overflow: hidden;
  }
  .sheet--cover { left: 91px; }
  .sheet--page { left: 649px; }

  .pattern {
    position: absolute;
    inset: 0;
    background: radial-gradient(circle at 50% 50%, var(--pattern-tint) 0%, var(--cream) 75%);
    opacity: 0.7;
  }
  .cover-title {
    position: absolute;
    left: 0;
    width: 100%;
    top: 66px;
    text-align: center;
    font-family: "Open Sans", sans-serif;
    color: var(--pastel-teal);
  }
  .cover-title__main {
    margin: 0;
    font-weight: 700;
    font-size: 32px;
    letter-spacing: -0.5px;
    line-height: 1;
  }
  .cover-title__sub {
    margin: 14px 0 0;
    font-weight: 300;
    font-size: 21px;
    line-height: 1;
  }
  .cover-art {
    position: absolute;
    left: 52px;
    top: 296px;
    width: 356px;
    height: 326px;
  }
  .page-rules {
    position: absolute;
    inset: 0;
  }
</style>
</head>
<body>
<main class="stage">
  <section class="sheet sheet--cover">
    <div class="pattern" role="img" aria-label="Faint repeating pattern of small hand-sketched Earth globes"></div>
    <header class="cover-title">
      <h1 class="cover-title__main">NOTEBOOK</h1>
      <p class="cover-title__sub">EARTH</p>
    </header>
    <svg class="cover-art" viewBox="0 0 356 326" role="img" aria-label="Large minimal sketch of planet Earth in pastel teal outline">
      <ellipse cx="178" cy="163" rx="176" ry="161" fill="var(--pastel-teal)" opacity="0.55"/>
    </svg>
  </section>

  <section class="sheet sheet--page">
    <div class="pattern" role="img" aria-label="Repeating pattern of small hand-sketched Earth globes"></div>
    <svg class="page-rules" viewBox="0 0 467 660" aria-hidden="true">
      <g stroke="var(--rule-blue)" stroke-width="1">
        <line x1="35" x2="433" y1="65" y2="65"/>
        <line x1="35" x2="433" y1="100" y2="100"/>
        <line x1="35" x2="433" y1="134" y2="134"/>
        <line x1="35" x2="433" y1="170" y2="170"/>
        <line x1="35" x2="433" y1="205" y2="205"/>
        <line x1="35" x2="433" y1="241" y2="241"/>
        <line x1="35" x2="433" y1="277" y2="277"/>
        <line x1="35" x2="433" y1="312" y2="312"/>
        <line x1="35" x2="433" y1="347" y2="347"/>
        <line x1="35" x2="433" y1="382" y2="382"/>
        <line x1="35" x2="433" y1="417" y2="417"/>
        <line x1="35" x2="433" y1="452" y2="452"/>
        <line x1="35" x2="433" y1="489" y2="489"/>
        <line x1="35" x2="433" y1="524" y2="524"/>
        <line x1="35" x2="433" y1="559" y2="559"/>
        <line x1="35" x2="433" y1="595" y2="595"/>
      </g>
    </svg>
  </section>
</main>
</body>
</html>
```